Corvane Supplies Business Card

Professional business card that stand out to our potential customers. Front and back with clean modern design

Industry/Entity Type

Oil and gas

Contact Information for Business Card

Name, address, website , office phone and cell number

Requirements
Must have
• Editable files for each employee

```html
<!DOCTYPE html>
<html lang="en">
<head>
<meta charset="utf-8">
<title>Corvane Supplies — Business Card</title>
<link href="https://fonts.googleapis.com/css2?family=Lexend:wght@400;500;600;700&display=swap" rel="stylesheet">
<style>
  :root {
    --page: #ffffff;
    --card: #ffffff;
    --red: #f40000;
    --cyan: #04b2d0;
    --ink: #1f1f1f;
    --shadow: rgba(0, 0, 0, 0.32);
  }
  * { box-sizing: border-box; margin: 0; padding: 0; }
  html, body {
    width: 1200px; height: 1200px; overflow: hidden;
    background: var(--page);
    font-family: "Lexend", "Helvetica Neue", Arial, sans-serif;
    color: var(--ink);
  }
  .sheet { position: relative; width: 1200px; height: 1200px; }
  .card {
    position: absolute; left: 181px; width: 845px; height: 482px;
    background: var(--card);
    box-shadow: 0 0 60px 10px var(--shadow);
  }
  .card--front { top: 94px; }
  .card--back { top: 630px; }

  .brand {
    position: absolute; display: flex; flex-direction: column; align-items: center;
    transform: translateX(-50%);
  }
  .brand__square { width: 58px; height: 58px; background: var(--red); }
  .brand__name {
    margin-top: 34px; font-weight: 700; font-size: 30px;
    letter-spacing: 0.04em; text-transform: uppercase; color: var(--red);
    white-space: nowrap;
  }
  .card--front .brand { left: 422px; top: 170px; }
  .card--back .brand { left: 226px; top: 187px; }

  .front__website {
    position: absolute; left: 585px; top: 422px;
    font-size: 19px; letter-spacing: 0.02em;
  }

  .contact { position: absolute; left: 475px; top: 115px; }
  .contact__name {
    font-weight: 600; font-size: 36px; letter-spacing: 0.14em; line-height: 1;
  }
  .contact__title { margin-top: 10px; font-weight: 500; font-size: 21px; letter-spacing: 0.01em; }
  .contact__address { margin-top: 18px; font-size: 20px; letter-spacing: -0.01em; }
  .contact__list { list-style: none; margin-top: 26px; }
  .contact__item { display: flex; align-items: center; height: 41px; }
  .contact__icon {
    width: 32px; height: 32px; border-radius: 50%; background: var(--cyan);
    display: flex; align-items: center; justify-content: center; margin-left: -3px;
  }
  .contact__text { margin-left: 19px; font-size: 21px; letter-spacing: 0.03em; }
  .contact__text--phone { letter-spacing: 0.14em; }
</style>
</head>
<body>
<main class="sheet">
  <section class="card card--front">
    <div class="brand">
      <div class="brand__square"></div>
      <div class="brand__name">Corvane Supplies</div>
    </div>
    <p class="front__website">www.yourwebsite.com</p>
  </section>

  <section class="card card--back">
    <div class="brand">
      <div class="brand__square"></div>
      <div class="brand__name">Corvane Supplies</div>
    </div>
    <div class="contact">
      <h1 class="contact__name">Your Name</h1>
      <p class="contact__title">Your Title</p>
      <p class="contact__address">Your Address and Country</p>
      <ul class="contact__list">
        <li class="contact__item">
          <span class="contact__icon">
            <svg width="18" height="18" viewBox="0 0 24 24" fill="#fff" aria-hidden="true"><path d="M6.6 10.8a15.1 15.1 0 0 0 6.6 6.6l2.2-2.2a1 1 0 0 1 1-.25 11.4 11.4 0 0 0 3.6.57 1 1 0 0 1 1 1V20a1 1 0 0 1-1 1A17 17 0 0 1 3 4a1 1 0 0 1 1-1h3.5a1 1 0 0 1 1 1c0 1.25.2 2.45.57 3.57a1 1 0 0 1-.25 1z"/></svg>
          </span>
          <span class="contact__text contact__text--phone">123-456-789</span>
        </li>
        <li class="contact__item">
          <span class="contact__icon">
            <svg width="20" height="20" viewBox="0 0 24 24" fill="none" stroke="#fff" stroke-width="1.6" aria-hidden="true"><circle cx="12" cy="12" r="9"/><ellipse cx="12" cy="12" rx="4" ry="9"/><path d="M3 12h18M5 7h14M5 17h14"/></svg>
          </span>
          <span class="contact__text">www.yourwebsite.com</span>
        </li>
        <li class="contact__item">
          <span class="contact__icon">
            <svg width="18" height="18" viewBox="0 0 24 24" fill="none" stroke="#fff" stroke-width="1.6" aria-hidden="true"><rect x="3" y="6" width="18" height="12"/><path d="M3 6l9 7 9-7M3 18l7-6M21 18l-7-6"/></svg>
          </span>
          <span class="contact__text">email@info.com</span>
        </li>
      </ul>
    </div>
  </section>
</main>
</body>
</html>
```